Automotive Repair Centre - Flyer Design

Bremwick Motors Cumbernauld are looking for a completely new flyer design for our blossoming auto repair centre. We are looking for bold eye catching designs as these flyers will be letterbox dropped around the local community. Approx. 10k per month. These will be printed double sided, on A5, with different print front and rear. Currently the whole rear is dedicated to servicing only, but this can be changed.

Our business prides itself on providing a high quality service so they flyer needs to convey this message. Also we believe in fair prices so they flyer also needs to convey this message in the design. Colour scheme is currently blue, yellow, and black. If possible it would be good to include the Drivemarq logo and the KELP logo.

We like the "specials" list from the Halvorn Drake flyer that is attached. We also like the clean look and layout of the other flyer that is uploaded. It would be good to include a special area for winter tyres much like is shown in the 50% off wheel alignment piece of the flyer attached.

Our current flyer uses the font GoodTimes as we would like this to remain if possible. It can be changed if the designer prefers. You can visit our website www.bremwick.co.uk for more information about our business.
Updates

Reason: Not had enough good designs to choose from yet.

Reason: Still not enough good designs to choose from

Reason: designs not up to the standard required.

Reason: Not enough designs that capture the brief have been submitted

Reason: looking for more designs

Reason: looking for some more bright designs. please read the brief!!!

Reason: same as before

Target Market(s)

General public.

Industry/Entity Type

Wheel

Requirements
Should not have
• We feel the flyer should not have photos of high end vehicles like Zantellis etc as the does not fit our approach of good value.

```html
<!DOCTYPE html>
<html lang="en">
<head>
<meta charset="utf-8">
<title>Bremwick Motors Cumbernauld – Flyer</title>
<link href="https://fonts.googleapis.com/css2?family=Orbitron:wght@500;700&family=Exo+2:ital,wght@0,500;0,600;1,800&display=swap" rel="stylesheet">
<style>
  :root {
    --navy: #08175e;
    --blue: #0d2c9a;
    --blue-mid: #1546c4;
    --blue-light: #2a6fe0;
    --yellow: #ffe21a;
    --bullet: #f7c948;
    --white: #ffffff;
  }
  html, body { margin: 0; padding: 0; overflow: hidden; background: #d9d9d9; }
  .flyer {
    position: relative; width: 856px; height: 1200px; overflow: hidden;
    background: linear-gradient(160deg, var(--blue) 0%, var(--navy) 100%);
    font-family: "Orbitron", sans-serif; color: var(--white);
  }
  .backdrop { position: absolute; inset: 0; }
  .abs { position: absolute; margin: 0; }
  .tagline {
    right: 46px; top: 56px; font-family: "Exo 2", sans-serif; font-style: italic;
    font-weight: 800; font-size: 37px; letter-spacing: -0.5px; white-space: nowrap;
  }
  .tagline .hl { color: var(--yellow); }
  .brand-name {
    left: 0; width: 856px; top: 222px; text-align: center; padding-left: 90px; box-sizing: border-box;
    font-weight: 700; font-size: 66px; letter-spacing: 1px;
  }
  .services { list-style: none; padding: 0; }
  .services li {
    position: absolute; font-weight: 500; font-size: 38px; line-height: 1;
    white-space: nowrap; display: flex; align-items: center;
  }
  .services li::before {
    content: ""; width: 24px; height: 24px; border-radius: 50%;
    background: var(--yellow); margin-right: 10px; flex: none;
  }
  .extras-title { right: 44px; top: 778px; color: var(--yellow); font-weight: 500; font-size: 23px; }
  .extras { list-style: none; padding: 0; right: 44px; top: 820px; text-align: right; }
  .extras li { font-weight: 500; font-size: 22px; line-height: 29px; white-space: nowrap; }
  .extras li::after {
    content: ""; display: inline-block; width: 11px; height: 11px; border-radius: 50%;
    background: var(--bullet); margin-left: 12px; vertical-align: 2px;
  }
  .contact { font-family: "Exo 2", sans-serif; font-weight: 600; font-size: 18px; }
  .address { left: 375px; top: 994px; line-height: 21.5px; }
  .address .line { padding-left: 12px; display: block; }
  .address svg { position: absolute; left: -2px; top: 4px; }
  .email, .web { top: 1097px; display: flex; align-items: center; gap: 7px; }
  .email { left: 375px; }
  .web { left: 628px; }
  .phone {
    left: 392px; top: 1126px; display: flex; align-items: center; gap: 12px;
    color: var(--yellow); font-weight: 500; font-size: 40px; letter-spacing: 2px;
  }
  .photo { position: absolute; border-radius: 50%; }
</style>
</head>
<body>
<main class="flyer">
  <svg class="backdrop" width="856" height="1200" viewBox="0 0 856 1200" aria-hidden="true">
    <defs>
      <linearGradient id="swoosh" x1="0" y1="0" x2="1" y2="1">
        <stop offset="0" stop-color="#2a6fe0"/><stop offset="1" stop-color="#0d2c9a"/>
      </linearGradient>
      <linearGradient id="band" x1="0" y1="0" x2="1" y2="0">
        <stop offset="0" stop-color="#1a55d0"/><stop offset="1" stop-color="#0f38a8"/>
      </linearGradient>
    </defs>
    <path d="M0 120 C 60 400, 40 800, 330 1200 L 260 1200 C 20 850, 10 450, 0 250 Z" fill="url(#swoosh)" opacity="0.7"/>
    <path d="M60 0 C 0 300, 80 700, 420 1200 L 380 1200 C 40 720, -30 320, 20 0 Z" fill="#1a4fcc" opacity="0.55"/>
    <path d="M310 1200 C 500 1060, 700 1010, 856 1010 L 856 1200 Z" fill="url(#band)"/>
    <path d="M350 1200 C 520 1090, 700 1050, 856 1050" fill="none" stroke="#3b82f0" stroke-width="3" opacity="0.6"/>
  </svg>

  <div class="photo" role="img" aria-label="Photo of the repair centre building front under a blue sky"
       style="left:130px;top:70px;width:700px;height:330px;border-radius:0;background:radial-gradient(ellipse at 60% 50%, rgba(70,120,220,0.55), rgba(13,44,154,0) 70%);"></div>

  <p class="abs tagline">YOU DRIVE <span class="hl">IT</span> WE <span class="hl">FIX IT</span></p>
  <h1 class="abs brand-name">BREMWICK</h1>

  <div class="photo" role="img" aria-label="Photo of gloved hands holding a diagnostic scanner in an engine bay"
       style="left:33px;top:405px;width:236px;height:140px;background:radial-gradient(ellipse, #8a6f5a 0%, #3a3040 60%, #1b1c30 100%);"></div>
  <div class="photo" role="img" aria-label="Photo of a mechanic's hands using a spanner on engine parts"
       style="left:70px;top:559px;width:286px;height:170px;background:radial-gradient(ellipse, #b88a6a 0%, #6b5a50 55%, #2a2630 100%);"></div>
  <div class="photo" role="img" aria-label="Photo of a mechanic in a blue shirt working underneath a car"
       style="left:116px;top:753px;width:352px;height:206px;background:radial-gradient(ellipse at 45% 55%, #5b86c9 0%, #3a4a70 50%, #161a2a 100%);"></div>

  <ul class="abs services" style="left:0;top:0;">
    <li style="left:287px;top:417px;">MOT $35</li>
    <li style="left:323px;top:473px;">SERVICING $89</li>
    <li style="left:362px;top:531px;">TYRES</li>
    <li style="left:389px;top:588px;">BRAKES</li>
    <li style="left:427px;top:644px;">EXHAUSTS</li>
    <li style="left:470px;top:700px;">CLUTCHES</li>
  </ul>

  <p class="abs extras-title">WE ALSO PROVIDE:</p>
  <ul class="abs extras">
    <li>FAULT DIAGNOSTICS</li>
    <li>BATTERIES</li>
    <li>WHEEL ALIGNMENT</li>
    <li>WELDING</li>
    <li>&amp; MORE</li>
  </ul>

  <address class="abs contact address" style="font-style:normal;">
    <svg width="10" height="14" viewBox="0 0 10 14" aria-hidden="true"><path d="M5 0a5 5 0 0 1 5 5c0 3.5-5 9-5 9S0 8.5 0 5a5 5 0 0 1 5-5z" fill="#7fb0ff"/><circle cx="5" cy="5" r="2" fill="#0d2c9a"/></svg>
    <span class="line">14-16 Carrow Place</span>
    <span class="line">Northfield Industrial Estate</span>
    <span class="line">Cumbernauld</span>
    <span class="line">G67 4QX</span>
  </address>

  <p class="abs contact email">
    <svg width="18" height="13" viewBox="0 0 18 13" aria-hidden="true"><rect x="1" y="1" width="16" height="11" fill="none" stroke="#7fb0ff" stroke-width="1.5"/><path d="M1 1l8 6 8-6" fill="none" stroke="#7fb0ff" stroke-width="1.5"/></svg>
    sales@bremwick.co.uk
  </p>
  <p class="abs contact web">
    <svg width="16" height="16" viewBox="0 0 16 16" aria-hidden="true"><g fill="none" stroke="#7fb0ff" stroke-width="1.2"><circle cx="8" cy="8" r="7"/><ellipse cx="8" cy="8" rx="3" ry="7"/><path d="M1 8h14M2.5 4.5h11M2.5 11.5h11"/></g></svg>
    www.bremwick.co.uk
  </p>

  <p class="abs phone">
    <svg width="36" height="36" viewBox="0 0 36 36" aria-hidden="true"><circle cx="18" cy="18" r="16" fill="none" stroke="#ffffff" stroke-width="2"/><path d="M13 9c-2 1-3 3-2 6 1.5 5 5 9.5 10 12 2.5 1 4.5 0 5.5-2l-3-3.5-2.5 1.5c-2.5-1.5-4.5-4-5.5-6.5l2-2z" fill="#ffffff"/></svg>
    01236 500482
  </p>
</main>
</body>
</html>
```